Talking Points for Clinic Visits tri-fold brochure

We are looking for a 1 page (front and back) 8.5" x 11" tri-fold brochure. Please refer back to our Rack Cards for a similar look and feel to the design. They can be found here: https://venmorelink.org/resources/fresh-plate-steady-mind-rack-card-series/.
This brochure is titled: Talking Points for Clinic Visits on Recall Lapses.

The document is for older readers. Do not put text over graphics and keep it simple and easy to read with high contrast.

We want some very simple design element(s) incorporated that convey Native American communities or heritage. But NO headdress, teepee graphics, owls etc. I have included some images, please use your creative discretion to use which ones look good.

Please remember to include the funding statement - it can be in a very small font 6/7 point: For more information about our project, please visit https://venmorelink.org/mind-care/resources - This rack card is supported by the Bureau for Illness Tracking and Safeguards (BITS) of the Federal Office of Wellness and Civic Aid (OWCA) as part of a financial assistance award totaling $1,053,119.36 with 100 percent funded by BITS/OWCA. The contents are those of the author(s) and do not necessarily represent the official views of, nor an endorsement, by BITS/OWCA, or the U.S. Government.

Please feel free to choose one of each of the 2 logos that looks best (horizontal or square). We have the VL7 logo and the Mind Care Support Hub logo we would like to add. I have added the document and there are images to choose from to use.

I am thinking that the front of the tri-fold should have one of the pictures of a patient and doctor talking. I have included several options. Please use your creative discretion to choose what looks best.

Please let me know if you have any questions, thank you!

```html
<!DOCTYPE html>
<html lang="en">
<head>
<meta charset="utf-8">
<title>Talking Points for Clinic Visits on Recall Lapses – Tri-fold Brochure</title>
<link href="https://fonts.googleapis.com/css2?family=Montserrat:wght@600;700;800&family=Open+Sans:wght@400;600;700&display=swap" rel="stylesheet">
<style>
  :root{
    --teal:#3a98a2;
    --teal-dark:#2b7c86;
    --rust:#b55a4e;
    --rust-dark:#9c4a40;
    --ink:#2b2b2b;
    --muted:#555;
    --paper:#ffffff;
    --stage:#dcdcdc;
    --row:#eaf4f5;
  }
  *{box-sizing:border-box;margin:0;padding:0}
  html,body{width:1200px;height:3000px;overflow:hidden;background:var(--stage)}
  body{position:relative;font-family:"Open Sans",Arial,sans-serif;color:var(--ink)}
  .spread{position:absolute;left:40px;width:1120px;height:866px;background:var(--paper);
    display:grid;grid-template-columns:repeat(3,1fr);box-shadow:0 2px 6px rgba(0,0,0,.12)}
  .spread--outside{top:594px}
  .spread--inside{top:1540px}
  .panel{position:relative;overflow:hidden;display:flex;flex-direction:column}
  .panel + .panel{border-left:1px solid #eee}
  .artwork{width:100%}
  h2,h3{font-family:"Montserrat",Arial,sans-serif}
  .heading{font-weight:800;text-transform:uppercase;line-height:1.15}
  .heading--rust{color:var(--rust)}
  .heading--teal{color:var(--teal)}

  /* Outside – intro panel */
  .intro{padding:34px 30px 24px;font-size:14px;line-height:1.55}
  .intro-art{flex:1;background:linear-gradient(160deg,var(--teal) 0%,#6fa9a6 30%,#b89a6a 60%,#8a6a45 100%)}

  /* Outside – resources panel */
  .resources{padding:34px 30px 0}
  .resources .heading{font-size:27px;margin-bottom:22px;text-align:center}
  .resource{margin-bottom:16px;text-align:center}
  .resource-title{font-weight:700;font-size:14px;line-height:1.3}
  .resource-link{font-size:12.5px;color:var(--teal-dark)}
  .funding{margin:auto 0 0;background:var(--teal);color:#fff;padding:18px 26px 22px}
  .funding h3{font-size:14px;margin-bottom:6px;text-align:center}
  .funding p{font-size:9.5px;line-height:1.45}

  /* Outside – cover */
  .brand{display:flex;align-items:center;gap:10px;padding:26px 28px 18px}
  .brand-mark{width:34px;height:34px;background:var(--teal);flex:none}
  .brand-name{font-family:"Montserrat",Arial,sans-serif;font-weight:700;font-size:13px;color:var(--teal-dark);line-height:1.2;text-transform:uppercase}
  .cover-photo{height:330px;background:linear-gradient(120deg,#e9e3dc 0%,#b9a48f 45%,#6b5a4d 100%)}
  .cover-band{flex:1;background:var(--rust);color:#fff;padding:40px 30px;display:flex;flex-direction:column;justify-content:center;align-items:center;gap:26px;text-align:center}
  .cover-band .heading{font-size:27px}
  .url-pill{background:var(--teal);color:#fff;font-weight:700;font-size:15px;padding:9px 22px;border-radius:22px}

  /* Inside – questions panel */
  .questions{padding:34px 30px 10px}
  .questions .heading{font-size:24px;margin-bottom:20px}
  .question{font-weight:700;font-size:14.5px;margin-bottom:12px;line-height:1.35}
  .subhead{font-family:"Montserrat",Arial,sans-serif;font-weight:700;color:var(--teal);font-size:16px;margin:18px 0 10px}
  .two-col{display:grid;grid-template-columns:1fr 1fr;gap:6px 14px;list-style:none;font-size:13px}
  .two-col li{padding-left:14px;position:relative}
  .two-col li::before{content:"";position:absolute;left:0;top:7px;width:6px;height:6px;border-radius:50%;background:var(--rust)}
  .trees-art{flex:1;background:linear-gradient(90deg,#5e9a3e 0%,#8dbb4a 35%,#e3b33c 65%,#c9622c 100%);margin-top:16px}

  /* Inside – doctor asks panel */
  .hands-art{height:330px;background:linear-gradient(150deg,#6a8fa0 0%,#b98a6a 40%,#c9623f 100%)}
  .asks{flex:1;background:var(--rust);color:#fff;padding:30px 28px}
  .asks .heading{font-size:24px;margin-bottom:12px}
  .asks p{font-size:14px;margin-bottom:16px}
  .asks .two-col{font-size:13.5px;gap:12px 14px}
  .asks .two-col li::before{background:#fff}

  /* Inside – tracker panel */
  .idea-art{height:250px;background:radial-gradient(circle at 50% 55%,#f3d7b5 0%,#e9b6a8 35%,#f7f1ec 75%)}
  .tracker{padding:20px 28px}
  .tracker .heading{font-size:24px;margin-bottom:8px}
  .tracker p{font-size:13px;line-height:1.5;margin-bottom:12px}
  .tracker table{width:100%;border-collapse:collapse;font-size:12.5px}
  .tracker th{background:var(--teal);color:#fff;padding:7px 6px;text-align:left;font-weight:700}
  .tracker td{height:30px;border-bottom:1px solid #cfe3e5}
  .tracker tr:nth-child(even) td{background:var(--row)}
  .tracker .note{font-size:12px;color:var(--muted);margin-top:12px}
</style>
</head>
<body>

<!-- Outside of brochure -->
<section class="spread spread--outside">
  <div class="panel">
    <div class="intro">
      <p>Memory changes can be worrying for elders and their families. Talking openly with a doctor is an important first step. Bring this brochure to your visit and use the questions inside to guide the talk. Write down your answers and share them with someone you trust.</p>
    </div>
    <div class="artwork intro-art" role="img" aria-label="Photograph of woven dry grasses and basket reeds on a teal background"></div>
  </div>

  <div class="panel">
    <div class="resources">
      <h2 class="heading heading--rust">For More Information About Memory Loss</h2>
      <div class="resource"><div class="resource-title">10 Signs of Changes in Memory and Thinking</div><div class="resource-link">www.venmorelink.org/signs</div></div>
      <div class="resource"><div class="resource-title">Knowing Which Doctor to See</div><div class="resource-link">www.venmorelink.org/doctors</div></div>
      <div class="resource"><div class="resource-title">Help Line for Memory Concerns</div><div class="resource-link">www.venmorelink.org/helpline</div></div>
      <div class="resource"><div class="resource-title">Caring for a Loved One at Home</div><div class="resource-link">www.venmorelink.org/caring</div></div>
      <div class="resource"><div class="resource-title">Pathways to Well-Being with Memory Loss</div><div class="resource-link">www.venmorelink.org/pathways</div></div>
    </div>
    <div class="funding">
      <h3>Funding Statement</h3>
      <p>For more information about our project, please visit https://venmorelink.org/mind-care/resources - This rack card is supported by the Bureau for Illness Tracking and Safeguards (BITS) of the Federal Office of Wellness and Civic Aid (OWCA) as part of a financial assistance award totaling $1,053,119.36 with 100 percent funded by BITS/OWCA. The contents are those of the author(s) and do not necessarily represent the official views of, nor an endorsement, by BITS/OWCA, or the U.S. Government.</p>
    </div>
  </div>

  <div class="panel">
    <div class="brand">
      <span class="brand-mark"></span>
      <span class="brand-name">Venmore Link Alliance for Elder Wellness</span>
    </div>
    <div class="artwork cover-photo" role="img" aria-label="Photograph of a doctor showing a tablet to an older patient"></div>
    <div class="cover-band">
      <h1 class="heading" style="font-family:'Montserrat',Arial,sans-serif;font-size:27px">Talking Points for Clinic Visits on Recall Lapses</h1>
      <span class="url-pill">www.venmorelink.org</span>
    </div>
  </div>
</section>

<!-- Inside of brochure -->
<section class="spread spread--inside">
  <div class="panel">
    <div class="questions">
      <h2 class="heading heading--teal">Talking Points for Clinic Visits</h2>
      <p class="question">When should I be concerned?</p>
      <p class="question">What kind of testing can be done for memory loss?</p>
      <p class="question">What other things could be causing memory loss?</p>
      <p class="question">Are there treatments that can help?</p>
      <p class="question">What can I do to keep my mind healthy?</p>
      <h3 class="subhead">What happens after diagnosis?</h3>
      <ul class="two-col">
        <li>Follow-up visits</li><li>Care planning</li>
        <li>Support groups</li><li>Family meetings</li>
        <li>Medication review</li><li>Safety at home</li>
        <li>Legal planning</li><li>Community services</li>
      </ul>
    </div>
    <div class="artwork trees-art" role="img" aria-label="Illustration of four trees shaped like heads, changing from green to autumn colours"></div>
  </div>

  <div class="panel">
    <div class="artwork hands-art" role="img" aria-label="Photograph of an elder's hands held by a caring hand"></div>
    <div class="asks">
      <h2 class="heading">Questions Your Doctor May Ask You</h2>
      <p>Your doctor may ask you about daily life and health.</p>
      <ul class="two-col">
        <li>How is your sleep?</li><li>Have you felt sad or down?</li>
        <li>Do you lose things often?</li><li>Are you taking any medicines?</li>
        <li>Have you had any falls?</li><li>Do you get lost in familiar places?</li>
        <li>Is it hard to manage money?</li><li>How much do you drink?</li>
      </ul>
    </div>
  </div>

  <div class="panel">
    <div class="artwork idea-art" role="img" aria-label="Illustration of a head in profile with a light bulb and gears"></div>
    <div class="tracker">
      <h2 class="heading heading--teal">Symptom Tracker</h2>
      <p>Use this chart to track memory changes you notice. Write the date, what happened and how long it lasted. Bring the chart to your next visit.</p>
      <table>
        <thead><tr><th>Date</th><th>What Happened</th><th>How Long</th></tr></thead>
        <tbody>
          <tr><td></td><td></td><td></td></tr>
          <tr><td></td><td></td><td></td></tr>
          <tr><td></td><td></td><td></td></tr>
          <tr><td></td><td></td><td></td></tr>
          <tr><td></td><td></td><td></td></tr>
          <tr><td></td><td></td><td></td></tr>
        </tbody>
      </table>
      <p class="note">Share this tracker with your doctor and a family member.</p>
    </div>
  </div>
</section>

</body>
</html>
```